Personal Branding - Pilot, Blogger, Speaker

I need a unique card that is remarkable and fits around me and my personal brand. I am an airline captain, blogger, and speaker. I want the card to have some element that is so unique the recipient will have to show someone else how bizarre and unique it is. I also want to stay within the bounds of professionalism. My card will be given out to other airlines to get a better flying job as well as people I want to come to my blog and hire me to speak at their event. I speak on motivation, life goals, learning, and time management. My brand is to inspire others to conquer fear and live remarkably. I want to include the color orange in my design.
Updates

My website is www.corwinteller.com to get an idea of who I am am what my brand is. I am a motivational speaker, blogger, and entrepreneur. My day job is a captain at an airline. I want to include the following info on my business card. I saw a card that had a crazy mouth on the back and when you hold it in front of your mouth it looks like you're making a silly face. Just one catchy idea I saw and liked. I really want something worth making a remark about when I walk away.Thank You for your designs. Orange, Black, Gray, Red, Corwin T. Teller Captain Valtrix 320 Skyloom Airlines 555.283.6094 corwinteller.com corwinteller@mailvale.net Speaker, Blogger, Entrepreneur

Reason: Extension to allow all designers time to complete their projects. Thank you for your designs. Incredible talent.

I've increased the budget of this project because I've shifted my focus slightly. I am including some links here to design ideas that I want to work towards. On the left side of a light gray card I want "corwinteller.com" in this font. I'm not sure if all black or black and red mix of letters will look best. Maybe the .com will be red https://cdn4.zq-img.net/entries/812/604337/2281-907-5521093877ab1c3d04e77f19/QX2_thumb.jpg This website will be the primary focus of the card. To drive traffic to my platform. (the original photo from https://www.tasklantern.net/contest/Logo-Design-for-blue-kite-NET-812.html) From the same photo I want the orange streak to come out of the bottom of the "b" in my name and arc back up and through the "o" in .com I want the rocket to be above the website name and flying upwards and to the right of the card. I like the angle of the rocket in the photo, it just needs to be flying the other direction so it passes through the letter "o" I like the colors of gray background, red rocket, orange streak. My contact info in black font will be below this logo and on the lower right of the card: Corwin T. Teller Captain, VTX-320, Skyloom Airlines 555.283.6094 corwinteller@mailvale.net On the back of the card is just this quote in black on a white background and the words "LIVE YOUR LEGEND" The quote will be in black letters and the "LIVE YOUR LEGEND" will be in red letters. β€œIt’s what you have always wanted to accomplish. Everyone, when they are young, knows what their Personal Legend is. At that point in their lives, everything is clear and everything is possible. They are not afraid to dream, and to yearn for everything they would like to see happen to them in their lives. But, as time passes, a mysterious force begins to convince them that it will be impossible for them to realize their Personal Legend.” ― Marten Vosk, The Lamplighter LIVE YOUR LEGEND. I'll try to submit a sketch somewhere on here. Thank You!!!

```html
<!DOCTYPE html>
<html lang="en">
<head>
<meta charset="utf-8">
<title>Corwin T. Teller – Business Card</title>
<link rel="stylesheet" href="https://fonts.googleapis.com/css2?family=Open+Sans:wght@400;600;700&display=swap">
<style>
  :root {
    --canvas-bg: #2b2f36;
    --card-front-light: #f4f4f4;
    --card-front-mid: #d9d9d9;
    --card-front-dark: #bdbdbd;
    --card-back: #ffffff;
    --ink: #111111;
    --accent-red: #d4141c;
    --accent-orange: #f28c13;
  }
  * { box-sizing: border-box; margin: 0; padding: 0; }
  html, body {
    width: 1200px;
    height: 800px;
    overflow: hidden;
    background: var(--canvas-bg);
    font-family: "Open Sans", Arial, sans-serif;
    color: var(--ink);
  }
  .card-set {
    width: 1200px;
    height: 800px;
    display: flex;
    align-items: center;
    justify-content: center;
    gap: 40px;
  }
  .card {
    width: 540px;
    height: 310px;
    position: relative;
    border-radius: 4px;
    box-shadow: 0 14px 30px rgba(0,0,0,0.45);
  }

  /* Back: quote */
  .card-back {
    background: var(--card-back);
    padding: 34px 44px 28px 70px;
  }
  .quote-mark {
    position: absolute;
    font-weight: 700;
    font-size: 64px;
    line-height: 1;
    color: var(--ink);
  }
  .quote-mark--open { left: 22px; top: 18px; }
  .quote-mark--close { left: 300px; top: 172px; }
  .quote-text {
    font-size: 13px;
    line-height: 1.45;
    text-align: justify;
    width: 420px;
  }
  .quote-source {
    position: absolute;
    right: 44px;
    bottom: 48px;
    font-size: 14px;
    font-weight: 600;
    text-align: right;
  }
  .quote-tagline {
    position: absolute;
    right: 44px;
    bottom: 26px;
    font-size: 14px;
    font-weight: 400;
    letter-spacing: 0.5px;
    color: var(--accent-red);
  }

  /* Front: identity */
  .card-front {
    background: radial-gradient(ellipse at 45% 35%, var(--card-front-light) 0%, var(--card-front-mid) 60%, var(--card-front-dark) 100%);
  }
  .brand {
    position: absolute;
    left: 44px;
    top: 92px;
    display: flex;
    align-items: center;
    gap: 14px;
  }
  .brand-name {
    font-size: 44px;
    font-weight: 400;
    letter-spacing: 0.5px;
    color: var(--ink);
  }
  .brand-dot {
    width: 22px;
    height: 22px;
    border-radius: 50%;
    background: var(--accent-orange);
  }
  .contact {
    position: absolute;
    right: 30px;
    bottom: 26px;
    text-align: right;
    font-size: 14px;
    line-height: 1.5;
  }
  .contact-name { font-weight: 700; }
  .contact-role { color: var(--accent-red); font-weight: 400; }
</style>
</head>
<body>
  <main class="card-set">
    <section class="card card-back" aria-label="Card back with quote">
      <span class="quote-mark quote-mark--open">“</span>
      <p class="quote-text">It’s the thing you have always meant to pursue. Everyone, when they start out, knows which road they want to travel. At that moment in their lives, the path looks bright and every door seems open. They are not afraid to hope, and to reach for everything they would like to build for themselves along the way. But, as the years go by, a quiet doubt begins to persuade them that it will be too late for them to follow their own road.</p>
      <span class="quote-mark quote-mark--close">”</span>
      <p class="quote-source">— Marten Vosk, The Lamplighter</p>
      <p class="quote-tagline">LIVE THE LEGEND.</p>
    </section>

    <section class="card card-front" aria-label="Card front with contact details">
      <div class="brand">
        <span class="brand-name">corwinteller.com</span>
        <span class="brand-dot"></span>
      </div>
      <div class="contact">
        <p><span class="contact-name">Corwin T. Teller</span> <span class="contact-role">Captain</span></p>
        <p>VTX-320, Skyloom Airlines 555.283.6094</p>
        <p>corwinteller@mailvale.net</p>
      </div>
    </section>
  </main>
</body>
</html>
```